hi all

Im after a new age looking business card with my company logo on it

must include these details, I would like the PH and Email to be symbols

If the colours used for card could be kept within the colours used in logo that I have supplied that would be great, if another colour is to be used dark grey would be ok. no light bulbs etc thanks

Details below to be incorporated on card

Damian Holloway

Lic E871302

PH 0219647381

E info@brightvaleelectrical.example.nz

Domestic Commercial Industrial Electricians

```html
<!DOCTYPE html>
<html lang="en">
<head>
<meta charset="utf-8">
<title>Brightvale Electrical – Business Card</title>
<link href="https://fonts.googleapis.com/css2?family=Exo+2:wght@300;400;800&family=Michroma&display=swap" rel="stylesheet">
<style>
  :root {
    --backdrop: #d1d2d4;
    --brand-blue: #1177bf;
    --card-light: #f1f1f3;
    --dark-grey: #474747;
    --text-grey: #6b6b6b;
    --divider: #8a8a8a;
    --white: #ffffff;
  }
  * { margin: 0; padding: 0; box-sizing: border-box; }
  html, body {
    width: 1200px; height: 800px; overflow: hidden;
    background: var(--backdrop);
  }
  .canvas { position: relative; width: 1200px; height: 800px; }

  .card { position: absolute; width: 534px; height: 306px; overflow: hidden; }
  .card--front { left: 318px; top: 74px; background: var(--brand-blue); }
  .card--back { left: 321px; top: 420px; background: var(--card-light); }

  .brand {
    position: absolute; display: flex; flex-direction: column; align-items: center;
    font-family: "Michroma", sans-serif; line-height: 1;
  }
  .brand__dot { width: 30px; height: 30px; border-radius: 50%; margin-bottom: 12px; }
  .brand__name { font-size: 22px; letter-spacing: 0.5px; }
  .brand__sub { font-size: 8px; letter-spacing: 2.5px; margin-top: 6px; align-self: flex-end; }

  .card--front .brand { left: 0; right: 0; top: 116px; color: var(--white); }
  .card--front .brand__dot { background: var(--white); }
  .card--front .brand__inner { display: flex; flex-direction: column; align-items: center; }

  .card--back .brand { left: 42px; width: 178px; top: 150px; color: var(--brand-blue); }
  .card--back .brand__dot { background: var(--brand-blue); }

  .tagline {
    position: absolute; left: 0; right: 0; top: 280px; text-align: center;
    font-family: "Exo 2", sans-serif; font-weight: 400; font-size: 11.5px;
    letter-spacing: 2.6px; color: var(--white);
  }

  .divider {
    position: absolute; left: 257px; top: 64px; width: 2px; height: 174px;
    background: var(--divider);
  }

  .contact { position: absolute; left: 265px; top: 100px; font-family: "Exo 2", sans-serif; }
  .contact__name {
    font-weight: 800; font-size: 24px; letter-spacing: 1.2px; color: var(--brand-blue);
    margin-bottom: 10px;
  }
  .contact__row {
    display: flex; align-items: center; gap: 8px; height: 24px;
    color: var(--text-grey); font-weight: 300; font-size: 18px; letter-spacing: 0.6px;
  }
  .contact__row--email { font-size: 13.5px; letter-spacing: 0.1px; }
  .contact__icon { width: 18px; height: 20px; flex: none; }

  .footer-bands { position: absolute; left: 0; bottom: 0; width: 534px; height: 20px; }
</style>
</head>
<body>
<main class="canvas">

  <section class="card card--front" aria-label="Card front">
    <div class="brand">
      <div class="brand__inner">
        <span class="brand__dot"></span>
        <span class="brand__name">BRIGHTVALE</span>
        <span class="brand__sub">ELECTRICAL</span>
      </div>
    </div>
    <p class="tagline">Domestic Commercial Industrial Electricians</p>
  </section>

  <section class="card card--back" aria-label="Card back">
    <div class="brand">
      <span class="brand__dot"></span>
      <span class="brand__name">BRIGHTVALE</span>
      <span class="brand__sub">ELECTRICAL</span>
    </div>

    <div class="divider"></div>

    <div class="contact">
      <h1 class="contact__name">Damian Holloway</h1>
      <p class="contact__row">
        <svg class="contact__icon" viewBox="0 0 18 20" aria-hidden="true">
          <circle cx="9" cy="7" r="5.5" fill="none" stroke="#1177bf" stroke-width="1.6"/>
          <path d="M5.5 11.5 V19 L9 16.5 L12.5 19 V11.5" fill="none" stroke="#1177bf" stroke-width="1.6" stroke-linejoin="round"/>
        </svg>
        E871302
      </p>
      <p class="contact__row">
        <svg class="contact__icon" viewBox="0 0 18 20" aria-hidden="true">
          <path d="M4 3 L7 3 L8.5 7 L6.5 8.5 C7.5 10.8 9 12.4 11.3 13.5 L12.8 11.5 L16.5 13 L16.5 16 C16.5 17 15.7 17.5 14.8 17.5 C8.5 17 3.5 12 3 5 C3 4 3.3 3 4 3 Z" fill="#1177bf"/>
        </svg>
        0219647381
      </p>
      <p class="contact__row contact__row--email">
        <svg class="contact__icon" viewBox="0 0 18 20" aria-hidden="true">
          <rect x="1" y="5" width="16" height="11" fill="none" stroke="#1177bf" stroke-width="1.5"/>
          <path d="M1 5 L9 11.5 L17 5 M1 16 L7 10 M17 16 L11 10" fill="none" stroke="#1177bf" stroke-width="1.5"/>
        </svg>
        info@brightvaleelectrical.example.nz
      </p>
    </div>

    <svg class="footer-bands" viewBox="0 0 534 20" aria-hidden="true">
      <polygon points="264,12 534,12 534,20 256,20" fill="#1177bf"/>
      <polygon points="0,2 288,2 270,20 0,20" fill="#474747"/>
    </svg>
  </section>

</main>
</body>
</html>
```